Scrap Metal Company Require Brochure for presentation to prospective client

We are a scrap metal company based in Singapore.
We require a brochure of about 4 pages, 1) Cover Page, 2 and 3 is the material we deal in and services we provide and 4) a backpage.
Brochure will be presented to prospective and selected local supplier to present to them the type of products we deal in and the type of services we provide. Purpose is to convince the prospective client to engage our services and also to sell us their scrap metal.
http://www.pelrowanmetals.com/our-services/for-corporate <- This link is for the intended audience of this brochure.
Designer is welcome to take any images from my website or use their own images in the design. Preferably, should the designer choose to use scrap metal images, please try to mainly use pictures of aluminium scrap, copper scrap, stainless steel scrap and ferrous scrap.
Attached is our company logo and some pictures of the scrap. www.pelrowanmetals.com is our website.
The design should give the audience a feeling of confidence, professionalism, honesty and trust in us.
This brochure is intended to be A4 Sizer
Target Market(s)
Local manufacturing company that does metal fabrication with off-cut scrap during the manufacturing process
Industry/Entity Type
Steel
Look and feel

```html
<!DOCTYPE html>
<html lang="en">
<head>
<meta charset="utf-8">
<title>Pelrowan Metals Recycling – Inside Spread</title>
<link href="https://fonts.googleapis.com/css2?family=Lato:wght@400;700&display=swap" rel="stylesheet">
<style>
  :root {
    --backdrop-top: #cfcdcd;
    --backdrop-bottom: #b4b4b4;
    --paper: #ffffff;
    --body-text: #555555;
    --heading-gold: #d08a1a;
    --brand-gold: #c8921e;
    --label-ink: #111111;
    --ferrous-bar: #3b4048;
    --steel-bar: #d5d2cb;
    --copper-bar: #a3553b;
    --aluminum-bar: #9aa6a7;
  }
  * { margin: 0; padding: 0; box-sizing: border-box; }
  html, body { width: 1200px; height: 1200px; overflow: hidden; }
  body {
    position: relative;
    background: linear-gradient(180deg, var(--backdrop-top), var(--backdrop-bottom));
    font-family: "Lato", Arial, sans-serif;
    color: var(--body-text);
  }
  .page {
    position: absolute;
    top: 139px;
    width: 536px;
    height: 758px;
    background: var(--paper);
  }
  .page--left { left: 54px; }
  .page--right { left: 623px; }

  .page-label {
    position: absolute;
    top: 927px;
    width: 536px;
    text-align: center;
    font-weight: 700;
    font-size: 24px;
    letter-spacing: 0.3px;
    color: var(--label-ink);
  }
  .page-label--left { left: 54px; }
  .page-label--right { left: 623px; }

  /* material strip */
  .material-strip {
    position: absolute;
    left: 11px; top: 0;
    width: 514px; height: 147px;
    display: flex;
    border: 1px solid #333;
  }
  .material { flex: 1; display: flex; flex-direction: column; }
  .material__name {
    height: 18px;
    line-height: 18px;
    text-align: center;
    font-weight: 700;
    font-size: 12.5px;
    color: #fff;
  }
  .material__photo { flex: 1; }
  .material--ferrous .material__name { background: var(--ferrous-bar); }
  .material--ferrous .material__photo { background: linear-gradient(135deg, #5a6470, #aeb5bd 45%, #4b5560); }
  .material--steel .material__name { background: var(--steel-bar); color: #111; }
  .material--steel .material__photo { background: linear-gradient(135deg, #6e5a48, #b9ad9c 40%, #3d342c); }
  .material--copper .material__name { background: var(--copper-bar); }
  .material--copper .material__photo { background: linear-gradient(135deg, #5a2a18, #c9784a 45%, #6b3420); }
  .material--aluminum .material__name { background: var(--aluminum-bar); color: #111; }
  .material--aluminum .material__photo { background: linear-gradient(135deg, #8b8f8d, #d2d4d1 50%, #6e7270); }

  /* brand */
  .brand {
    position: absolute;
    left: 43px; top: 213px;
    width: 120px;
    text-align: center;
  }
  .brand__square {
    display: block;
    width: 32px; height: 32px;
    margin: 0 auto 10px;
    border: 2px solid var(--brand-gold);
  }
  .brand__name {
    font-weight: 700;
    font-size: 11px;
    letter-spacing: 0.6px;
    color: var(--brand-gold);
    line-height: 13px;
  }

  .copy {
    position: absolute;
    font-size: 9.4px;
    line-height: 9.95px;
  }
  .copy p { margin-bottom: 9.95px; }
  .copy--justified { text-align: justify; }

  .intro-a { left: 195px; top: 212px; width: 141px; }
  .intro-b { left: 362px; top: 212px; width: 136px; }

  .hero-photo {
    position: absolute;
    left: 12px; top: 0;
    width: 513px; height: 146px;
    background: linear-gradient(160deg, #4a3e30, #b3a48a 35%, #6b5d49 60%, #d2c7b2 80%, #3c3226);
  }

  .section-title {
    position: absolute;
    top: 196px;
    font-weight: 700;
    font-size: 16.5px;
    color: var(--heading-gold);
    letter-spacing: 0.2px;
  }
  .products-title { left: 32px; }
  .services-title { left: 205px; }

  .products { left: 32px; top: 224px; width: 155px; }
  .products .step { text-transform: uppercase; font-size: 9.6px; }
  .services { left: 205px; top: 224px; width: 147px; }
  .services-more { left: 370px; top: 224px; width: 139px; }
</style>
</head>
<body>

<section class="page page--left">
  <div class="material-strip">
    <div class="material material--ferrous"><div class="material__name">FERROUS</div><div class="material__photo" role="img" aria-label="Stacked ferrous box-section beams"></div></div>
    <div class="material material--steel"><div class="material__name">STEEL</div><div class="material__photo" role="img" aria-label="Pile of steel sheet scrap"></div></div>
    <div class="material material--copper"><div class="material__name">COPPER</div><div class="material__photo" role="img" aria-label="Coils of copper wire scrap"></div></div>
    <div class="material material--aluminum"><div class="material__name">ALUMINUM</div><div class="material__photo" role="img" aria-label="Stacked aluminum sheet scrap"></div></div>
  </div>

  <div class="brand">
    <span class="brand__square"></span>
    <div class="brand__name">PELROWAN METALS RECYCLING</div>
  </div>

  <div class="copy intro-a">
    <p>Pelrowan Metals Recycling primary activities are the procurement, processing, recycling and trading of all ferrous and non-ferrous scrap metals, industrial scraps and other recyclables.</p>
    <p>We provide full-service ferrous and non-ferrous metal recycler and processor. Recognized as an industry leader in metal recycling, our team of experienced staff and trader understand the intricacies of scrap metal recycling.</p>
    <p>We build long term relationships with all our customer by understanding their needs and recommending customized solutions that are designed to improve efficiency and value of their scrap.</p>
    <p>In the ever changing market environment, we constantly improve every aspect of our company, delivering consistent and reliable service and products to our clientele. Call us today to see how we can serve you.</p>
  </div>

  <div class="copy intro-b">
    <p>Pelrowan Metals Recycling is a privately-held company located in Singapore with a humble beginning. We has grown rapidly through the continuous support of our customer and suppliers and currently have supplier across various industries including, general public, constructions, manufacturers, engineering, demolition, shipyards, other recycling yards and overseas customer.</p>
    <p>Pelrowan Metals Recycling has become a recycling industry leader in the local market, committed to responsibly and efficiently serving all its customer, supplier and community with integrity and professionalism, and in an environmentally safe manner.</p>
    <p>We are committed to our suppliers and consumers by effectively sourcing, processing, and marketing scrap metal for recycling. We actively pursue new and long lasting relationships by partnering with our customers, providing quality service built upon integrity, honesty, and professionalism. We are committed to meeting all our customers needs by exceeding their expectations.</p>
  </div>
</section>

<section class="page page--right">
  <div class="hero-photo" role="img" aria-label="Heap of cut metal plate scrap"></div>

  <h2 class="section-title products-title">PRODUCTS</h2>
  <h2 class="section-title services-title">SERVICES</h2>

  <div class="copy products">
    <p class="step">Process</p>
    <p class="step">Procurement &amp; Collection</p>
    <p>Purchase from both our local (companies &amp; individual)and overseas sources for transporting of scrap material to our scrap yard.</p>
    <p class="step">Sorting &amp; Segregation</p>
    <p>At our yard, all items will be sorted into different categories and grade.</p>
    <p class="step">Ferrous Scrap</p>
    <p>After sorting and segregation, all ferrous scrap will be shear and cut to improve density and remove of other impurities.</p>
    <p class="step">Non-Ferrous Scrap</p>
    <p>All non-ferrous scrap will be processed to remove any impurities and subsequently, send for baling barquetting or packing into jumbo bags.</p>
    <p class="step">Quality Control</p>
    <p>Both ferrous and non-ferrous scrap will be inspected closely to ensure the quality of the processed scrap material.</p>
    <p class="step">Storage/Sale</p>
    <p>Item will be stored within our premises or sent to our buyers.</p>
  </div>

  <div class="copy copy--justified services">
    <p>Pelrowan Metals Recycling provides excellent service and very competitive pricing for your scrap materials. Some of the services we provide are as follows:</p>
    <p>Roll-off Open Top Container (OTC), small container, customized container for the disposal of your scrap material at your premises. Arrangement can also be made should you require container to be place at other permanent or temporary work site.</p>
    <p>Fast and convenient service for collection. We provide regular schedule pick-up or just call us when the bin is full!</p>
    <p>Our company provide weighing upon collection with our accurately calibrated crane scale so you always know the weight of your material before leaving the premises.</p>
    <p>Should your company scrap contain confidential information, or rejected material that requires to be destroy, you are welcome to visit our scrap yard to witness the destruction process, alternatively, we can send you a photographic image as proof.</p>
  </div>

  <div class="copy copy--justified services-more">
    <p>We provide prompt payment and very competitive price. Even if you need payment upon collection, just let us know.</p>
    <p>Should you have other requirement on top of your scrap collection, e.g. waste collection, we will be more than please to offer any solutions or to accommodate to your request.</p>
    <p>Companies are also welcome to unload their scrap material at our scrap yard.</p>
    <p>Write us an email here or fill up the form below today to understand how we can be at your service or for a non-obliging quotation for your scrap material. We will contact you promptly!</p>
  </div>
</section>

<div class="page-label page-label--left">INSIDE LEFT</div>
<div class="page-label page-label--right">INSIDE RIGHT</div>

</body>
</html>
```